BRIGHTWAVE PARTNERS NAMECARD

Need to design a name card with an existing logo.

As we are professional corporate services provider our name card has to project a professional image.
Should be corporate, simple & professional.

Our corporate color is maroon red but not too dull.

Please refer to our website at www.brightwavepartners.com.sg

Would attach our logo herewith.

Front surface of namecard details:
BRIGHTWAVE PARTNERS PTE LTD
Registration No. 208731945K

Lowe Hui Ting CA (Singapore)
Director

Tel +65 6481 2957
Mobile +65 9172 3806
lowe@brightwavepartners.com.sg
www.brightwavepartners.com.sg

47 Palmer Lane
#07-14 Harbourlight Plaza
Singapore 274153

Back of namecard:-
OUR CORE SERVICES
Incorporation services
Corporate Secretarial Services
Accountancy service
Goods & Services Taxation
Corporate & Personal Taxation
Financial Reporting
Payroll Administration

AFFILIATES:
TRIVANTA CORPORATE SERVICES PTE LTD
BRIGHTWAVEREGISTRYPTE LTD
ORR MANAGEMENT SERVICES PTE LTD
DW LIM AND COMPANY PTE LTD
LEDGERWISE ACADEMY

```html
<!DOCTYPE html>
<html lang="en">
<head>
<meta charset="utf-8">
<title>Brightwave Partners Namecard</title>
<link rel="stylesheet" href="https://fonts.googleapis.com/css2?family=Open+Sans:wght@400;600;700&family=Tinos:wght@400;700&display=swap">
<style>
  :root {
    --stage: #141414;
    --paper: #fbf9f5;
    --brand-red: #d0202f;
    --ink: #2b2b2b;
    --ink-soft: #555555;
    --band-dark: #2e2e2e;
  }
  * { box-sizing: border-box; margin: 0; padding: 0; }
  html, body { width: 1200px; height: 1000px; overflow: hidden; background: var(--stage); }
  .stage { position: relative; width: 1200px; height: 1000px; }
  .card {
    position: absolute; width: 510px; height: 292px; background: var(--paper);
    box-shadow: 0 10px 30px rgba(0,0,0,.6); overflow: hidden;
    font-family: "Open Sans", Arial, sans-serif; color: var(--ink);
  }
  .card--front { left: 60px; top: 150px; }
  .card--back { left: 630px; top: 520px; }

  .brand-name {
    font-family: "Open Sans", Arial, sans-serif; font-weight: 700;
    color: var(--brand-red); font-size: 17px; line-height: 21px;
  }

  /* front */
  .front-rule { position: absolute; left: 34px; top: 90px; width: 270px; height: 2px; background: var(--brand-red); }
  .card--front .brand-name { position: absolute; left: 316px; top: 78px; }
  .holder { position: absolute; left: 34px; top: 40px; }
  .holder-name { font-family: "Tinos", "Times New Roman", serif; font-size: 15px; color: var(--brand-red); }
  .holder-cred { color: var(--ink-soft); }
  .holder-role { font-family: "Open Sans", Arial, sans-serif; font-size: 12px; color: var(--ink); margin-top: 1px; }
  .contacts { position: absolute; left: 34px; top: 112px; list-style: none; font-size: 11px; line-height: 17px; }
  .contacts li { display: flex; align-items: center; gap: 8px; }
  .contacts svg { width: 10px; height: 10px; fill: var(--brand-red); flex: none; }
  .address { position: absolute; right: 30px; bottom: 30px; text-align: right; font-size: 11.5px; font-weight: 600; line-height: 17px; font-style: normal; }

  /* back */
  .card--back .brand-name { position: absolute; left: 30px; top: 26px; }
  .back-rule { position: absolute; left: 200px; top: 72px; right: 30px; height: 2px; background: var(--brand-red); transform-origin: left; }
  .section-title { font-size: 12px; font-weight: 700; color: var(--brand-red); text-transform: uppercase; margin-bottom: 5px; }
  .affiliates { position: absolute; left: 30px; top: 84px; }
  .affiliates ul, .services ul { list-style: none; }
  .affiliates li { font-size: 10.5px; line-height: 14px; }
  .services { position: absolute; right: 30px; top: 112px; width: 210px; }
  .services li { font-size: 12px; line-height: 15px; }
  .footer-band { position: absolute; left: 0; bottom: 0; width: 100%; height: 40px; }
</style>
</head>
<body>
<main class="stage">

  <section class="card card--front" aria-label="Namecard front">
    <div class="front-rule"></div>
    <div class="brand-name">Brightwave<br>Partners</div>
    <div class="holder">
      <p class="holder-name">Lowe Hui Ting <span class="holder-cred">CA (Singapore)</span></p>
      <p class="holder-role">Director</p>
    </div>
    <ul class="contacts">
      <li><svg viewBox="0 0 10 10"><path d="M2 0.5 3.6 2.6 2.7 3.8C3.3 5 4.8 6.6 6.2 7.3L7.4 6.4 9.5 8 8.3 9.5C4.5 9.3 0.7 5.5 0.5 1.7Z"/></svg>+65 6481 2957</li>
      <li><svg viewBox="0 0 10 10"><path d="M2.5 0h5v10h-5zM3.3 1v7h3.4V1z"/></svg>+65 9172 3806</li>
      <li><svg viewBox="0 0 10 10"><path d="M0 2h10v6H0zM0.6 2.4 5 5.6 9.4 2.4"/></svg>lowe@brightwavepartners.com.sg</li>
      <li><svg viewBox="0 0 10 10"><path d="M5 0a5 5 0 1 0 0 10A5 5 0 0 0 5 0zm0 1a4 4 0 0 1 0 8 4 4 0 0 1 0-8zM1 4.6h8v.8H1zM4.6 1h.8v8h-.8z"/></svg>www.brightwavepartners.com.sg</li>
    </ul>
    <address class="address">47 Palmer Lane<br>#07-14 Harbourlight Plaza<br>Singapore 274153</address>
  </section>

  <section class="card card--back" aria-label="Namecard back">
    <div class="brand-name">Brightwave<br>Partners</div>
    <div class="back-rule"></div>
    <div class="affiliates">
      <h2 class="section-title">Affiliates</h2>
      <ul>
        <li>Trivanta Corporate Services Pte Ltd</li>
        <li>Brightwaveregistrypte Ltd</li>
        <li>Orr Management Services Pte Ltd</li>
        <li>Dw Lim And Company Pte Ltd</li>
        <li>Ledgerwise Academy</li>
      </ul>
    </div>
    <div class="services">
      <h2 class="section-title">Core Services</h2>
      <ul>
        <li>Incorporation Services</li>
        <li>Corporate Secretarial Services</li>
        <li>Accountancy Service</li>
        <li>Goods &amp; Services Taxation</li>
        <li>Corporate &amp; Personal Taxation</li>
        <li>Financial Reporting</li>
        <li>Payroll Administration</li>
      </ul>
    </div>
    <svg class="footer-band" viewBox="0 0 510 40" preserveAspectRatio="none" aria-hidden="true">
      <rect x="0" y="28" width="510" height="12" fill="var(--band-dark)"/>
      <path d="M0 0H210Q232 0 232 22V40H0Z" fill="var(--brand-red)"/>
    </svg>
  </section>

</main>
</body>
</html>
```